Professional Facebook Banner, Business Cards, Door Hang Tags, Service Flyer for Pest Control Company

There are really 4 things I need designed but Pixel Harbor doesn't have them to package together. I am needing to get a Professional Facebook Banner, Business Cards, Door Hang Tags, and Service Flyer for a Pest Control Company. I already have a logo that I will attach to the project along with content a for each one of these tasks. Please see document attached labeled All Design Content & Flyer Content.
Pest Control

```html
<!DOCTYPE html>
<html lang="en">
<head>
<meta charset="utf-8">
<title>Ember Grove Pest Control – Brand Set</title>
<link rel="stylesheet" href="https://fonts.googleapis.com/css2?family=Roboto:wght@400;500;700;900&family=Open+Sans:wght@400;700&display=swap">
<style>
:root{
  --orange:#f26f2c;
  --ink:#070707;
  --paper:#ffffff;
  --red:#d8282b;
  --grey:#3a3a3a;
}
*{margin:0;padding:0;box-sizing:border-box}
html,body{width:1200px;height:893px;overflow:hidden;background:var(--paper)}
body{position:relative;font-family:"Roboto",Arial,sans-serif;color:var(--ink)}
.piece{position:absolute;overflow:hidden}
.abs{position:absolute}

/* brand name stand-in */
.brand{position:absolute;font-family:"Roboto",Arial,sans-serif;font-weight:900;color:var(--orange);text-align:center;line-height:1;letter-spacing:.02em}
.brand small{display:block;font-size:.42em;letter-spacing:.55em;margin-top:.25em}

/* ---------- facebook banner ---------- */
.banner{left:59px;top:18px;width:767px;height:336px;background:var(--ink)}
.banner-title{position:absolute;left:53px;top:93px;font-weight:900;font-size:44px;line-height:1;color:var(--paper);white-space:nowrap}
.banner-title.second{left:64px;top:138px}
.banner-headline{position:absolute;left:424px;top:105px;font-weight:900;font-size:32px;color:var(--paper);white-space:nowrap}
.banner-tagline{position:absolute;left:428px;top:138px;font-weight:700;font-size:19px;color:var(--orange);white-space:nowrap}
.book-now{position:absolute;left:357px;top:203px;width:128px;height:28px;border-radius:14px;background:var(--paper);color:var(--orange);font-weight:500;font-size:19px;display:flex;align-items:center;justify-content:center}
.banner-contact{position:absolute;left:345px;display:flex;align-items:center;gap:22px;color:var(--paper);font-size:12px}
.banner-rule{position:absolute;left:333px;top:299px;width:182px;height:5px;border-radius:3px;background:var(--orange)}
.art{position:absolute}

/* ---------- service flyer ---------- */
.flyer{left:899px;top:22px;width:234px;height:362px;background:var(--paper);font-family:"Open Sans",Arial,sans-serif}
.flyer-copy{position:absolute;left:0;width:234px;font-size:3.6px;line-height:1.45;color:var(--ink)}
.flyer-copy p{margin-bottom:3px}
.plan{position:absolute;border-radius:10px;color:var(--paper);font-size:3.6px;line-height:1.75}
.plan.orange{background:var(--orange)}
.plan.black{background:var(--ink)}
.plan h3{font-family:"Roboto",Arial,sans-serif;font-weight:700;font-size:6.5px;text-align:center;margin-top:4px}
.plan .col{position:absolute}
.plan .line{position:absolute;font-size:4px}
.plan b{font-weight:700}
.flyer-note{position:absolute;left:3px;top:348px;width:230px;font-size:3.4px;line-height:1.6}

/* ---------- business card front ---------- */
.card-front{left:87px;top:385px;width:399px;height:227px;background:var(--ink)}

/* ---------- services list ---------- */
.services{left:83px;top:662px;width:200px;height:175px}
.services-head{display:flex;align-items:center;gap:0}
.services-head i{display:block;width:14px;height:13px}
.services-head span{margin-left:5px;font-weight:700;font-size:11px;white-space:nowrap}
.services ul{list-style:none;margin:17px 0 0 23px}
.services li{position:relative;font-size:11px;line-height:14.2px;padding-left:13px}
.services li::before{content:"";position:absolute;left:0;top:3px;width:8px;height:8px;border-radius:50%;background:var(--orange)}

/* ---------- business card back ---------- */
.card-back{left:295px;top:636px;width:193px;height:230px;background:var(--ink);color:var(--paper)}
.card-name{position:absolute;left:15px;top:100px;font-weight:700;font-size:19px;white-space:nowrap}
.card-name span{color:var(--orange)}
.card-line{position:absolute;left:15px;font-size:11px;white-space:nowrap}
.card-strip{left:272px;top:734px;width:23px;height:98px;background:var(--orange)}

/* ---------- door hangers ---------- */
.hanger{top:436px;background:var(--paper)}
.hanger-copy{position:absolute;left:14px;width:130px;font-size:5.2px;line-height:1.3;text-align:justify}
.hanger-copy p{margin-bottom:6px}
.phone-pill{position:absolute;height:23px;border-radius:12px;background:var(--ink);border:2px solid var(--orange);color:var(--paper);font-weight:700;font-size:11px;display:flex;align-items:center;justify-content:center;gap:5px}
.offer{position:absolute;left:0;width:100%;text-align:center;font-weight:900;font-size:26px;color:var(--orange);line-height:1}
.offer-sub{position:absolute;left:0;width:100%;text-align:center;font-weight:700;font-size:8.5px;color:var(--orange)}
.offer-fine{position:absolute;left:0;width:100%;text-align:center;font-weight:700;font-size:7px}
.hanger-url{position:absolute;left:0;width:100%;text-align:center;font-size:7px;color:var(--paper)}
.hanger-url b{font-weight:700}
.services-box{position:absolute;left:10px;top:149px;width:138px;height:147px;border:2px solid var(--ink);border-radius:6px}
.services-box h4{position:absolute;top:-8px;left:22px;padding:0 4px;background:var(--paper);font-weight:700;font-size:11px;white-space:nowrap}
.svc{position:absolute;display:flex;align-items:flex-start;gap:4px;font-size:8.5px;line-height:1.15}
.svc svg{flex:none}
</style>
</head>
<body>

<!-- Facebook banner -->
<section class="piece banner" aria-label="Facebook banner">
  <svg class="art" width="767" height="336" viewBox="0 0 767 336" aria-hidden="true">
    <polygon points="0,0 199,0 262,336 0,336" fill="var(--orange)"/>
    <circle cx="0" cy="284" r="62" fill="var(--ink)"/>
    <path d="M0,120 A52,52 0 0 1 0,290" fill="none" stroke="var(--paper)" stroke-width="0.8" opacity=".8"/>
    <circle cx="764" cy="270" r="65" fill="var(--orange)"/>
    <path d="M767,150 A70,70 0 0 0 710,230" fill="none" stroke="var(--paper)" stroke-width="0.8"/>
    <rect x="105" y="233" width="70" height="62" fill="var(--ink)"/>
    <rect x="95" y="223" width="70" height="62" fill="var(--paper)"/>
    <rect x="166" y="265" width="70" height="62" fill="var(--ink)"/>
    <rect x="156" y="255" width="70" height="62" fill="var(--paper)"/>
  </svg>
  <div class="art" role="img" aria-label="Decorative dot pattern" style="left:678px;top:1px;width:89px;height:89px;border-radius:0 0 0 60px;background:radial-gradient(circle,#3d3d3d 0,#1b1b1b 70%);opacity:.8"></div>
  <div class="art" role="img" aria-label="Tick illustration" style="left:22px;top:58px;width:46px;height:32px;border-radius:50%;background:var(--ink)"></div>
  <div class="banner-title">EMBER GROVE</div>
  <div class="banner-title second">PEST CONTROL</div>

  <div class="brand" style="left:495px;top:50px;width:167px;font-size:17px">EMBER GROVE<small>PEST CONTROL</small></div>
  <div class="art" role="img" aria-label="Ant illustration" style="left:517px;top:88px;width:48px;height:18px;border-radius:9px;background:#e9e9e9"></div>
  <div class="banner-headline">INSECT PROBLEM ?</div>
  <div class="banner-tagline">Call us, we’re always on the go</div>
  <div class="book-now">BOOK NOW</div>
  <div class="banner-contact" style="top:246px">
    <svg width="14" height="14" viewBox="0 0 24 24" aria-hidden="true"><path d="M6.6 10.8a15 15 0 0 0 6.6 6.6l2.2-2.2c.3-.3.7-.4 1-.2 1.1.4 2.3.6 3.6.6.6 0 1 .4 1 1V20c0 .6-.4 1-1 1A17 17 0 0 1 3 4c0-.6.4-1 1-1h3.5c.6 0 1 .4 1 1 0 1.3.2 2.5.6 3.6.1.3 0 .7-.2 1z" fill="none" stroke="var(--paper)" stroke-width="1.8"/></svg>
    <span>555-014-2870</span>
  </div>
  <div class="banner-contact" style="top:271px;gap:20px">
    <svg width="14" height="14" viewBox="0 0 24 24" aria-hidden="true"><circle cx="12" cy="12" r="10" fill="none" stroke="var(--paper)" stroke-width="1.8"/><path d="M2 12h20M12 2c3 3 3 17 0 20M12 2c-3 3-3 17 0 20" fill="none" stroke="var(--paper)" stroke-width="1.5"/></svg>
    <span>www.embergrovepest.com</span>
  </div>
  <div class="banner-rule"></div>
</section>

<!-- Service flyer -->
<section class="piece flyer" aria-label="Service plans flyer">
  <div class="brand" style="left:70px;top:8px;width:94px;font-size:9px">EMBER GROVE<small>PEST CONTROL</small></div>
  <div class="flyer-copy" style="top:39px">
    <p>Pests are constantly trying to enter your home, which can easily cause frustration and damage to your home and belongings. That’s why we at Ember Grove Pest Control provide seasonally designed, proactive home pest control plans to protect your family and your home.</p>
    <p>Our home pest control plans offer effective and affordable solutions to all your pest issues in and around your home. If you have pest problems, schedule your free inspection today!</p>
    <p>Covered Pests: Ants, Carpenter Ants, Bees, Carpenter Bees, Box Elder Bugs, Centipedes, Clover Mites, Crickets, General Spiders, Ground Beetles, Earwigs, Millipedes, Mice, Oriental Roaches, Pill Bugs, Sow Bugs, Scorpions, and Wasps all within 10 feet of the structure being treated.</p>
  </div>

  <div class="plan orange" style="left:10px;top:104px;width:214px;height:64px">
    <h3>Home Defense Bronze</h3>
    <div class="col" style="left:16px;top:17px">Year <b>Round Pest Protection</b><br>Bi Monthly Service (6 visits per year)<br>Covers 15+ Pests<br>Exterior Treatment</div>
    <div class="col" style="left:127px;top:19px">Interior Treatment (As Needed)<br>Rodent Control<br><b>Stinging Insect Removal</b><br>Free Re Treatments</div>
    <div class="line" style="left:16px;top:49px;line-height:1.5">Termite Monitoring &amp;<br><b>Mosquito Reduction Treatments</b></div>
    <div class="line" style="left:103px;top:53px">$_________________________________</div>
  </div>
  <div class="plan black" style="left:9px;top:168px;width:216px;height:81px">
    <h3>Home Defense Silver</h3>
    <div class="col" style="left:18px;top:23px">Year <b>Round Pest Protection</b><br>Bi Monthly Service (6 visits per year)<br>Covers 15+ Pests<br>Exterior Treatment</div>
    <div class="col" style="left:127px;top:23px">Interior Treatment (As Needed)<br>Rodent Control<br><b>Stinging Insect Removal</b><br>Free Re Treatments</div>
    <div class="line" style="left:17px;top:60px;line-height:1.5">Termite Monitoring &amp;<br><b>Mosquito Reduction Treatments</b></div>
    <div class="line" style="left:106px;top:66px">$_________________________________</div>
  </div>
  <div class="plan orange" style="left:9px;top:250px;width:215px;height:88px">
    <h3>Home Defense Gold</h3>
    <div class="col" style="left:18px;top:24px">Year<b>Round Pest Protection</b><br>Bi Monthly Service (6 visits per year)<br>Covers 15+ Pests<br>Exterior Treatment</div>
    <div class="col" style="left:126px;top:23px">Interior Treatment (As Needed)<br>Rodent Control<br><b>Stinging Insect Removal</b><br>Free ReTreatments</div>
    <div class="line" style="left:16px;top:66px;line-height:1.5">Termite Monitoring &amp;<br><b>Mosquito Reduction Treatments</b></div>
    <div class="line" style="left:106px;top:74px">$_________________________________</div>
  </div>
  <div class="flyer-note">Please Note: to have full guarantee for Asian Beetles, Brown Recluse Spider, Cluster Flies, Lady Bugs, and Silverfish the structures attic and/or crawlspace would need to be treated. There are additional fees for theses services</div>
</section>

<!-- Business card front -->
<section class="piece card-front" aria-label="Business card front">
  <div class="brand" style="left:100px;top:95px;width:199px;font-size:25px">EMBER GROVE<small>PEST CONTROL</small></div>
</section>

<!-- Services list -->
<section class="piece services" aria-label="Services and inspections">
  <div class="services-head"><i style="background:var(--ink)"></i><i style="background:var(--orange)"></i><span>SERVICES / INSPECTIONS</span></div>
  <ul>
    <li>Ants</li><li>Mosquitos</li><li>Fleas</li><li>Roaches</li><li>Stinging Insects</li>
    <li>Spiders</li><li>Rodents</li><li>Termites</li><li>Mice</li><li>Rats</li>
  </ul>
</section>

<!-- Business card back -->
<div class="piece card-strip" aria-hidden="true">
  <svg width="23" height="98" viewBox="0 0 23 98">
    <circle cx="11.5" cy="12" r="4" fill="var(--paper)"/><path d="M4.5 24a7 6 0 0 1 14 0z" fill="var(--paper)"/>
    <path d="M7 40c1 4 4 7 8 8l2-2-3-2-1 1c-1-1-2-2-3-3l1-1-2-3z" fill="none" stroke="var(--paper)" stroke-width="1.3"/>
    <rect x="5" y="60" width="13" height="9" fill="none" stroke="var(--paper)" stroke-width="1.3"/><path d="M5 60l6.5 5 6.5-5" fill="none" stroke="var(--paper)" stroke-width="1.3"/>
    <circle cx="11.5" cy="83" r="6" fill="none" stroke="var(--paper)" stroke-width="1.3"/><path d="M5.5 83h12M11.5 77c2 2 2 10 0 12M11.5 77c-2 2-2 10 0 12" fill="none" stroke="var(--paper)" stroke-width="1"/>
  </svg>
</div>
<section class="piece card-back" aria-label="Business card back">
  <div class="brand" style="left:33px;top:19px;width:127px;font-size:16px">EMBER GROVE<small>PEST CONTROL</small></div>
  <div class="card-name"><span>DANA</span> REYES</div>
  <div class="card-line" style="top:132px">555-014-2870</div>
  <div class="card-line" style="top:154px">dana@embergrovepest.com</div>
  <div class="card-line" style="top:173px">www.embergrovepest.com</div>
</section>

<!-- Door hanger: about -->
<section class="piece hanger" style="left:643px;width:157px;height:383px" aria-label="Door hanger, about us">
  <svg class="art" width="157" height="383" viewBox="0 0 157 383" aria-hidden="true">
    <path d="M0,0H157V131C110,100 50,98 0,128Z" fill="var(--ink)"/>
    <path d="M0,128C50,98 110,100 157,131" fill="none" stroke="var(--orange)" stroke-width="2"/>
    <path d="M0,352C50,357 110,356 157,348V383H0Z" fill="var(--ink)"/>
    <path d="M0,352C50,357 110,356 157,348" fill="none" stroke="var(--orange)" stroke-width="2"/>
  </svg>
  <div class="brand" style="left:25px;top:136px;width:107px;font-size:11px">EMBER GROVE<small>PEST CONTROL</small></div>
  <div class="hanger-copy" style="top:168px">
    <p>We are a locally owned and operated, with 10 years of industry experience our family is committed to delivering exceptional customer service and high-quality results. We strive for excellence in all that we do.</p>
    <p>We treat each and every customer like a member of our family. When you partner with us, you can enjoy hassle-free services, expert care, and peace of mind knowing you and your home are protected from pests for years to come.</p>
  </div>
  <div class="phone-pill" style="left:24px;top:256px;width:103px">
    <svg width="10" height="10" viewBox="0 0 24 24" aria-hidden="true"><path d="M6.6 10.8a15 15 0 0 0 6.6 6.6l2.2-2.2c.3-.3.7-.4 1-.2 1.1.4 2.3.6 3.6.6.6 0 1 .4 1 1V20c0 .6-.4 1-1 1A17 17 0 0 1 3 4c0-.6.4-1 1-1h3.5c.6 0 1 .4 1 1 0 1.3.2 2.5.6 3.6.1.3 0 .7-.2 1z" fill="var(--paper)"/></svg>555-014-2870</div>
  <div class="offer" style="top:298px">$50 OFF</div>
  <div class="offer-sub" style="top:324px">Initial Home Protection Plan</div>
  <div class="offer-fine" style="top:336px">Smaller Print – New Customers Only</div>
  <div class="hanger-url" style="top:368px">www.<b>embergrovepest</b>.com</div>
</section>

<!-- Door hanger: services -->
<section class="piece hanger" style="left:871px;width:160px;height:386px" aria-label="Door hanger, our services">
  <svg class="art" width="160" height="386" viewBox="0 0 160 386" aria-hidden="true">
    <path d="M0,0H160V134C110,100 50,100 0,129Z" fill="var(--ink)"/>
    <path d="M0,129C50,100 110,100 160,134" fill="none" stroke="var(--orange)" stroke-width="2"/>
    <path d="M0,352C50,362 110,360 160,352V386H0Z" fill="var(--ink)"/>
    <path d="M0,352C50,362 110,360 160,352" fill="none" stroke="var(--orange)" stroke-width="2"/>
  </svg>
  <div class="services-box">
    <h4>OUR SERVICES</h4>
    <div class="svc" style="left:3px;top:20px"><svg width="14" height="14" viewBox="0 0 14 14"><circle cx="7" cy="7" r="6" fill="none" stroke="var(--red)" stroke-width="1.4"/><path d="M3 3l8 8" stroke="var(--red)" stroke-width="1.4"/></svg>Termites</div>
    <div class="svc" style="left:3px;top:37px"><svg width="14" height="14" viewBox="0 0 14 14"><circle cx="7" cy="7" r="6" fill="none" stroke="var(--red)" stroke-width="1.4"/><path d="M3 3l8 8" stroke="var(--red)" stroke-width="1.4"/></svg>Mosquitos</div>
    <div class="svc" style="left:3px;top:54px"><svg width="14" height="14" viewBox="0 0 14 14"><circle cx="7" cy="7" r="6" fill="none" stroke="var(--red)" stroke-width="1.4"/><path d="M3 3l8 8" stroke="var(--red)" stroke-width="1.4"/></svg>Ants</div>
    <div class="svc" style="left:3px;top:72px"><svg width="14" height="14" viewBox="0 0 14 14"><circle cx="7" cy="7" r="6" fill="none" stroke="var(--red)" stroke-width="1.4"/><path d="M3 3l8 8" stroke="var(--red)" stroke-width="1.4"/></svg>Fleas<br>&amp; More</div>
    <div class="svc" style="left:75px;top:21px"><svg width="14" height="14" viewBox="0 0 14 14"><circle cx="7" cy="7" r="6" fill="none" stroke="var(--red)" stroke-width="1.4"/><path d="M3 3l8 8" stroke="var(--red)" stroke-width="1.4"/></svg>Spiders</div>
    <div class="svc" style="left:75px;top:37px"><svg width="14" height="14" viewBox="0 0 14 14"><circle cx="7" cy="7" r="6" fill="none" stroke="var(--red)" stroke-width="1.4"/><path d="M3 3l8 8" stroke="var(--red)" stroke-width="1.4"/></svg>Rodents</div>
    <div class="svc" style="left:75px;top:55px"><svg width="14" height="14" viewBox="0 0 14 14"><circle cx="7" cy="7" r="6" fill="none" stroke="var(--red)" stroke-width="1.4"/><path d="M3 3l8 8" stroke="var(--red)" stroke-width="1.4"/></svg>Roaches</div>
    <div class="svc" style="left:75px;top:71px"><svg width="14" height="14" viewBox="0 0 14 14"><circle cx="7" cy="7" r="6" fill="none" stroke="var(--red)" stroke-width="1.4"/><path d="M3 3l8 8" stroke="var(--red)" stroke-width="1.4"/></svg>Stinging<br>Insects</div>
  </div>
  <div class="phone-pill" style="left:26px;top:259px;width:105px">
    <svg width="10" height="10" viewBox="0 0 24 24" aria-hidden="true"><path d="M6.6 10.8a15 15 0 0 0 6.6 6.6l2.2-2.2c.3-.3.7-.4 1-.2 1.1.4 2.3.6 3.6.6.6 0 1 .4 1 1V20c0 .6-.4 1-1 1A17 17 0 0 1 3 4c0-.6.4-1 1-1h3.5c.6 0 1 .4 1 1 0 1.3.2 2.5.6 3.6.1.3 0 .7-.2 1z" fill="var(--paper)"/></svg>555-014-2870</div>
  <div class="offer" style="top:302px">$25 OFF</div>
  <div class="offer-sub" style="top:328px">One Time Service</div>
  <div class="offer-fine" style="top:339px">Smaller Print – New Customers Only</div>
  <div class="hanger-url" style="top:371px">www.<b>embergrovepest</b>.com</div>
</section>

</body>
</html>
```